Duel Business card

Want an edgy business card that shows both of our companies on each side of the card, OR both together with a cool design.

*Must be edgy: We have attached our two business logos. We are a bail bond and immigration bond company.

Would like the address on one side only.
Need Phone, cell, website, address, and Name

Company Name 1: Cellgate Release Partners
www.cellgatereleasepartners.example

Company Name 2: Borderline Surety Associates
www.borderlinesuretyassociates.example

These cards will need to be easily changeable so I can modify new employees

Target Market(s)

people in jail, takign imigrants out of jail and from being taken back to there country

Industry/Entity Type

Business

Requirements
Must have
• Include both logos attached

```html
<!DOCTYPE html>
<html lang="en">
<head>
<meta charset="utf-8">
<title>Business Card – Cellgate Release Partners &amp; Borderline Surety Associates</title>
<link rel="stylesheet" href="https://fonts.googleapis.com/css2?family=Lato:wght@400;900&display=swap">
<style>
  :root {
    --page-bg: #e9e6e1;
    --card-white: #f4f4f4;
    --ink: #2b2b2b;
    --royal: #1f35b8;
    --navy: #142a66;
    --gold: #e0bb1c;
    --red: #d8141c;
    --white: #ffffff;
  }
  * { box-sizing: border-box; margin: 0; padding: 0; }
  html, body {
    width: 1200px; height: 720px; overflow: hidden;
    background: var(--page-bg);
    font-family: "Lato", sans-serif;
  }
  .canvas {
    position: relative; width: 1200px; height: 720px;
  }
  .card {
    position: absolute; top: 206px;
    width: 540px; height: 308px;
    overflow: hidden;
    box-shadow: 0 6px 18px rgba(0,0,0,.18);
  }
  /* Front */
  .card-front { left: 40px; background: var(--card-white); }
  .front-brand {
    position: absolute; right: 28px; top: 30px;
    display: flex; align-items: center; gap: 10px;
  }
  .brand-name {
    font-weight: 900; text-transform: uppercase; letter-spacing: .5px;
    line-height: 1.05;
  }
  .front-brand .brand-name { color: var(--navy); font-size: 17px; text-align: right; width: 150px; }
  .brand-dot {
    width: 30px; height: 30px; border-radius: 50%; flex: none;
  }
  .front-brand .brand-dot { background: var(--gold); }
  .front-partner {
    position: absolute; right: 28px; top: 120px;
    display: flex; align-items: center; gap: 10px;
  }
  .front-partner .brand-name { color: var(--red); font-size: 13px; text-align: right; width: 130px; }
  .front-partner .brand-dot { background: var(--red); width: 26px; height: 26px; }
  .person-name {
    position: absolute; left: 34px; top: 126px;
    font-size: 26px; font-weight: 400; color: var(--ink);
  }
  .contact-list {
    position: absolute; left: 34px; top: 200px;
    list-style: none; font-size: 14.5px; color: var(--ink); line-height: 19px;
  }
  .contact-list li { display: flex; align-items: center; gap: 12px; }
  .contact-icon { width: 13px; height: 13px; flex: none; fill: var(--navy); }
  .contact-icon-blank { width: 13px; flex: none; }
  /* Back */
  .card-back { left: 620px; display: flex; }
  .back-panel { position: relative; width: 50%; height: 100%; }
  .panel-bail { background: var(--royal); }
  .panel-immigration { background: var(--navy); }
  .back-brand {
    position: absolute; left: 0; right: 0; top: 54px;
    display: flex; flex-direction: column; align-items: center; gap: 14px;
    text-align: center; padding: 0 18px;
  }
  .back-brand .brand-name { color: var(--white); font-size: 22px; }
  .back-brand .brand-dot { width: 54px; height: 54px; }
  .panel-bail .brand-dot { background: var(--gold); }
  .panel-immigration .brand-dot { background: var(--white); }
  .web-band {
    position: absolute; left: 0; right: 0; top: 196px; height: 26px;
    display: flex; align-items: center; justify-content: center;
    font-size: 11.5px; color: var(--white); white-space: nowrap;
  }
  .band-gold { background: var(--gold); }
  .band-red { background: var(--red); }
</style>
</head>
<body>
<main class="canvas">
  <section class="card card-front" aria-label="Card front">
    <div class="front-brand">
      <span class="brand-name">Cellgate Release Partners</span>
      <span class="brand-dot"></span>
    </div>
    <div class="front-partner">
      <span class="brand-name">Borderline Surety Associates</span>
      <span class="brand-dot"></span>
    </div>
    <h1 class="person-name">Dana Whitlow</h1>
    <ul class="contact-list">
      <li>
        <svg class="contact-icon" viewBox="0 0 16 16"><rect x="1" y="1" width="14" height="14" rx="2" fill="none" stroke="currentColor"/><path d="M4 4h3l1 2-1.5 1.2a6 6 0 0 0 2.3 2.3L10 8l2 1v3h-1A8 8 0 0 1 4 5z"/></svg>
        <span>0400 555 0192 ext 2210</span>
      </li>
      <li>
        <svg class="contact-icon" viewBox="0 0 16 16"><path d="M4 1h8a1 1 0 0 1 1 1v12a1 1 0 0 1-1 1H4a1 1 0 0 1-1-1V2a1 1 0 0 1 1-1zm1 2v8h6V3zm3 9.5a1 1 0 1 0 0 .01z"/></svg>
        <span>dana.whitlow@cellgaterelease.example</span>
      </li>
      <li>
        <span class="contact-icon-blank"></span>
        <span>www.cellgaterelease.example</span>
      </li>
      <li>
        <svg class="contact-icon" viewBox="0 0 16 16"><path d="M8 1l7 6.5h-2V15H9.5v-4h-3v4H3V7.5H1z"/></svg>
        <span>Suite 4, Harbor Row, Millbrook, QX2 7LD</span>
      </li>
    </ul>
  </section>

  <section class="card card-back" aria-label="Card back">
    <div class="back-panel panel-bail">
      <div class="back-brand">
        <span class="brand-dot"></span>
        <span class="brand-name">Cellgate Release Partners</span>
      </div>
      <div class="web-band band-gold">www.cellgatereleasepartners.example</div>
    </div>
    <div class="back-panel panel-immigration">
      <div class="back-brand">
        <span class="brand-dot"></span>
        <span class="brand-name">Borderline Surety Associates</span>
      </div>
      <div class="web-band band-red">www.borderlinesuretyassociates.example</div>
    </div>
  </section>
</main>
</body>
</html>
```